Brightwell has a great new logo - now we need a website!!

Brightwell has been in business for a long time and needs to start a new era. Additional to other changes being made in the business itself, Brightwell needs an overhaul of its entire branding. PART 1 is COMPLETE - we have our new logo!

Next step... new website! That's where you come in.

Brightwell provides a range of computer related services including computer maintenance, networking, sales & cloud services. We provide onsite (field) and remote support. Our customers range from homes to companies with 100+ computers. We pride ourselves on clear and honest communication.

We are a small business but want a professional yet easy-going look that shows the 'cool' side of having your computer system cared for. The website should exude trustworthiness and professionalism but still get comments like 'modern' and 'smart design'. We want our customers to feel that choosing any other company to maintain their system would be a 'geeky' choice.

We like clear thinking so an uncluttered, well organised structure is appreciated. Obvious references to calling or emailing us would be good so people dont need to search around for our contact details.

We look after both Orvane & Kelvantix operating systems so there needs to be universal appeal rather than a look associated with only one of these two brands.

We want to wow our current clients but also attract new ones so a focus on SEO is a must. And a focus on social media too with links/feeds to Chatterloop, blipcast and Workweave!

Have a look at www.brightwell-tech.com.au so you can see for yourself how much you can help us!

**Breathe new life into Brightwell's online presence!**

(We do have a separate website www.hubloomdesk.com.au that we set as the homepage for our clients - we like how it is but it might need freshening up to match our new site. We will also want our chatterloop page totally made over. You'll probably have other suggestions of things we should be doing. We want to form an ongoing relationship with the right designer!)

(Also, we are open to suggestions regarding the logo size and colour)
Updates

I dont want to cramp anyones creativity but i like this: http://www.quandrelweb.com/demo/themes/wordpress/2011/pebble/

I'm obivously happy to see your own ideas too!

I also like this one: http://layoutmarkt.net/item/zindo-responsive-wordpress-theme/7718205

Clarification: We are looking for a working, implemented website, not just design of the theme. Once the general page layout is done we can do the majority of the content input. But we do want a workable shell with images.

We are open to buying existing themes if that helps. Thanks!

Site also needs email contact form, testimonial submission page, blog (feed to home page), chatterloop like button

Reason: I haven't found the ideal one yet... We want some other designers to send their ideas.

Reason: We need a little more time to make our decision.

Target Market(s)

Mainly small to medium businesses but also homes

Industry/Entity Type

Small Business

Requirements
Must have
• SEO
Social Media
That little address bar icon
R in a circle at the bottom of the site to show we have trademarked our company name
A finished product website with content and images that we can modify ourselves over time.

```html
<!DOCTYPE html>
<html lang="en">
<head>
<meta charset="utf-8">
<title>Brightwell – IT Solutions & Support</title>
<link href="https://fonts.googleapis.com/css2?family=PT+Sans+Narrow:wght@400;700&family=PT+Sans:wght@400;700&family=Kalam:wght@700&display=swap" rel="stylesheet">
<style>
:root{
  --nav-blue:#4a5f98;
  --nav-dark:#3a4c80;
  --ink:#2f2f2f;
  --body:#555;
  --orange:#f0930f;
  --orange-light:#ffb52a;
  --sky:#0fa6e0;
  --navy:#10507d;
  --hero:#dcdcdc;
  --rule:#e3e3e3;
  --footer:#2f3436;
  --footer-text:#d8d8d8;
  --footer-head:#5b86c8;
}
*{margin:0;padding:0;box-sizing:border-box}
html,body{width:966px;height:1200px;overflow:hidden;background:#fff}
body{font-family:"PT Sans Narrow",sans-serif;color:var(--body)}
.page{position:relative;width:966px;height:1200px;overflow:hidden}
.abs{position:absolute}

/* navigation */
.topnav{left:0;top:0;width:966px;height:54px;background:linear-gradient(#5d71a8,var(--nav-blue) 60%,var(--nav-dark))}
.topnav ul{list-style:none;position:absolute;left:139px;top:13px;display:flex;gap:3px}
.topnav li{width:84px;height:32px;border:1px solid #7185bb;background:linear-gradient(#5467a0,#425690);color:#fff;font-weight:700;font-size:12px;letter-spacing:.6px;text-align:center;line-height:30px}
.topnav li.current{background:linear-gradient(#6f83b8,#5669a0);color:#1d2a4c}

/* header */
.brand{left:139px;top:80px;display:flex;align-items:center;gap:10px}
.brand-dot{width:40px;height:40px;border-radius:50%;background:var(--navy)}
.brand-name{font-family:"PT Sans",sans-serif;font-weight:700;font-size:28px;color:#333;letter-spacing:.5px}
.social{top:84px;width:31px;height:31px;border-radius:50%;display:flex;align-items:center;justify-content:center}

/* hero */
.hero{left:0;top:146px;width:966px;height:294px;background:linear-gradient(#d6d6d6,#e0e0e0 50%,#d2d2d2);border-top:4px solid #ececec;border-bottom:4px solid #ececec}
.hero-title{left:158px;top:178px;font-family:"Kalam",cursive;font-size:44px;color:#2a2a2a}
.hero-text{left:158px;top:250px;width:320px;font-size:12px;line-height:22px;letter-spacing:.4px;color:#666}
.cta{left:158px;top:339px;width:171px;height:43px;border-radius:3px;background:linear-gradient(var(--orange-light),var(--orange));border-bottom:3px solid #d8600e;color:#fff;font-weight:700;font-size:17px;text-align:center;line-height:40px;letter-spacing:.3px}
.hero-art{left:585px;top:158px;width:180px;height:262px;border-radius:90px 90px 12px 12px;background:radial-gradient(ellipse at 50% 30%,#6b8cc7,#3a5790 60%,#cfcfcf 100%)}

/* intro */
.tagline{left:0;top:456px;width:966px;text-align:center;font-weight:700;font-size:22px;color:#333;letter-spacing:.6px}
.tagline em{font-style:normal;color:var(--orange)}
.rule{height:1px;background:var(--rule)}

.feature{top:530px;width:220px}
.feature h3{display:flex;align-items:center;gap:10px;font-size:13px;font-weight:700;color:#333;letter-spacing:.5px;margin-left:-1px}
.feature .ico{width:28px;height:28px;border-radius:50%;display:flex;align-items:center;justify-content:center}
.feature p{margin-top:8px;font-size:10.3px;line-height:15.2px;color:#555}

.about h2{font-size:14px;font-weight:700;color:#333;letter-spacing:.4px}
.about ul{list-style:none;margin-top:8px}
.about li{font-size:10.5px;line-height:22px;color:#555;padding-left:17px;position:relative}
.about li::before{content:"›";position:absolute;left:0;color:var(--navy);font-weight:700}
.shot{top:665px;width:158px;height:107px;border:2px solid #b4b8be}

/* widgets */
.widget{top:838px;width:191px}
.widget-bar{height:22px;color:#fff;font-weight:700;font-size:14px;letter-spacing:.4px;display:flex;align-items:center;justify-content:center;gap:8px}
.widget .date{margin-top:10px;font-size:8.6px;letter-spacing:.4px;padding-left:2px}
.widget p{margin-top:4px;font-size:8.6px;line-height:15.2px;color:#555;padding-left:2px}
.widget .more{font-style:italic;font-size:8.6px;padding-left:2px}
.field{margin-top:10px;height:22px;border:1px solid #ccc;font-style:italic;font-size:8.4px;color:#888;padding:6px 8px}

/* footer */
.footer{left:0;top:992px;width:966px;height:208px;background:linear-gradient(var(--footer),#3d4345 50%,#2b3033);border-top:4px solid #4e5f90}
.foot-head{font-family:"PT Sans",sans-serif;font-size:8.5px;letter-spacing:.6px;color:var(--footer-head);padding-bottom:5px;border-bottom:1px solid #4b5154}
.foot-links{list-style:none;font-family:"PT Sans",sans-serif;font-size:8.5px;color:var(--footer-text)}
.foot-links li{line-height:16.6px;padding-left:13px;position:relative}
.foot-links li::before{content:"›";position:absolute;left:0;color:var(--footer-head)}
.fsoc{width:27px;height:27px;border-radius:50%;background:radial-gradient(circle at 40% 35%,#fff,#cfcfcf);display:flex;align-items:center;justify-content:center}
.copy{font-family:"PT Sans",sans-serif;font-size:8px;color:var(--footer-text);letter-spacing:.4px}
.flabel{font-family:"PT Sans",sans-serif;font-size:8px;color:var(--footer-text)}
.finput{background:#2a2e30;border:1px solid #4f5558}
.go{left:666px;top:1128px;width:42px;height:18px;background:linear-gradient(#5f78b5,#415a98);color:#fff;font-family:"PT Sans",sans-serif;font-size:8px;text-align:center;line-height:18px;letter-spacing:.5px}
</style>
</head>
<body>
<div class="page">

  <nav class="abs topnav">
    <ul>
      <li class="current">HOME</li><li>SERVICES</li><li>PRICING</li><li>HOURS</li><li>PAYMENTS</li><li>LINKS</li><li>NEWS</li><li>CONTACT</li>
    </ul>
  </nav>

  <header>
    <div class="abs brand"><span class="brand-dot"></span><span class="brand-name">Brightwell</span></div>
    <a class="abs social" style="left:672px;background:#0d4a76" aria-label="Chatterloop"></a>
    <a class="abs social" style="left:713px;background:#19a9e3" aria-label="Blipcast"></a>
    <a class="abs social" style="left:755px;background:#f08c16" aria-label="RSS">
      <svg width="14" height="14" viewBox="0 0 14 14" fill="#fff"><circle cx="2.5" cy="11.5" r="2"/><path d="M1 6a7 7 0 0 1 7 7h-2a5 5 0 0 0-5-5z"/><path d="M1 1a12 12 0 0 1 12 12h-2A10 10 0 0 0 1 3z"/></svg>
    </a>
    <a class="abs social" style="left:796px;background:#b9b9b9" aria-label="Email">
      <svg width="14" height="10" viewBox="0 0 14 10"><rect width="14" height="10" rx="1" fill="#fff"/><path d="M0 1l7 5 7-5" stroke="#b9b9b9" fill="none"/></svg>
    </a>
  </header>

  <section class="abs hero"></section>
  <h1 class="abs hero-title">Headline Title</h1>
  <p class="abs hero-text">Sed egestas, mi dignissim fringilla placerat, ligula justo laoreet dolor, rutrum faucibus felis neque sit amet dolor. Integer vel enim vitae justo lacinia venenatis vitae sit amet ante.</p>
  <a class="abs cta">GET SUPPORT NOW</a>
  <div class="abs hero-art" role="img" aria-label="Illustration of a friendly businessman in a blue suit thinking about a laptop"></div>

  <h2 class="abs tagline">Duis sagittis metus in quam <em>ornare ultrices oplening elli</em></h2>
  <div class="abs rule" style="left:139px;top:501px;width:689px"></div>

  <article class="abs feature" style="left:143px">
    <h3><span class="ico" style="background:var(--sky)"><svg width="16" height="12" viewBox="0 0 16 12" fill="#fff"><circle cx="5" cy="3" r="2.5"/><circle cx="11" cy="3" r="2.5"/><path d="M0 12c0-4 2-6 5-6s5 2 5 6zM8 12c0-3 1-5 3-6 3 0 5 2 5 6z"/></svg></span>CUSTOMER FOCUS</h3>
    <p>Fusce egestas luctus lacus vitae hendrerit. Morbi vitae nibh erat, non aliquet diam. Curabitur odio mauris, suscipit non blandit iaculis, tempor quis velit. Sed consequat justo et massa.</p>
  </article>
  <article class="abs feature" style="left:377px">
    <h3><span class="ico" style="background:var(--orange)"><svg width="14" height="14" viewBox="0 0 14 14" fill="none" stroke="#fff" stroke-width="1.4"><path d="M1 1v12h12"/><path d="M3 10l3-4 2 2 4-5"/></svg></span>SUPPORT</h3>
    <p>Fusce egestas luctus lacus vitae hendrerit. Morbi vitae nibh erat, non aliquet diam. Curabitur odio mauris, suscipit non blandit iaculis, tempor quis velit. Sed consequat justo et massa.</p>
  </article>
  <article class="abs feature" style="left:604px">
    <h3><span class="ico" style="background:var(--navy)"><svg width="14" height="14" viewBox="0 0 14 14" fill="none" stroke="#fff" stroke-width="1.3"><ellipse cx="6" cy="4" rx="5" ry="2"/><path d="M1 4v5c0 1 2 2 5 2"/><circle cx="10" cy="10" r="3"/></svg></span>COST EFFECTIVE</h3>
    <p>Fusce egestas luctus lacus vitae hendrerit. Morbi vitae nibh erat, non aliquet diam. Curabitur odio mauris, suscipit non blandit iaculis, tempor quis velit. Sed consequat justo et massa.</p>
  </article>

  <section class="abs about" style="left:143px;top:665px">
    <h2>About our Company</h2>
    <ul>
      <li>Fusce egestas luctus lacus vitae hen</li>
      <li>Morbi vitae nibh erat, non aliquet</li>
      <li>Curabitur odio mauris, suscipit non</li>
      <li>Sed consequat justo et bibendum</li>
    </ul>
  </section>
  <div class="abs shot" style="left:336px;background:linear-gradient(#a9c9c2,#8fb2ab)" role="img" aria-label="Illustration of two connected smartphones sharing messages"></div>
  <div class="abs shot" style="left:503px;background:radial-gradient(circle at 55% 45%,#5f7a6e,#2c3432)" role="img" aria-label="Illustration of a laptop with colourful arrows bursting out"></div>
  <div class="abs shot" style="left:669px;background:radial-gradient(circle at 50% 50%,#3d4f8f,#1a2356)" role="img" aria-label="Illustration of a presenter beside a chart on a screen"></div>

  <div class="abs rule" style="left:139px;top:807px;width:689px"></div>

  <section class="abs widget" style="left:138px">
    <div class="widget-bar" style="background:var(--sky)"><svg width="12" height="12"><circle cx="6" cy="6" r="5" fill="#fff"/></svg>blipcast feed</div>
    <div class="date" style="color:var(--sky)">12.12.12</div>
    <p>Luctus lacus vitae hendrerit. Morbi vitae nibh erat, non aliquet diam. Curabitur odio mauris, suscipit non erreting ise ondest 12 teresd en illde</p>
    <div class="more" style="color:var(--sky)">read more &gt;</div>
  </section>
  <section class="abs widget" style="left:387px">
    <div class="widget-bar" style="background:var(--orange)"><svg width="12" height="12" viewBox="0 0 12 12"><path d="M1 11l2-5 6-5 2 2-5 6z" fill="#fff"/></svg>latest blog</div>
    <div class="date" style="color:#333">12.12.12 BLOG TITLE</div>
    <p>Luctus lacus vitae hendrerit. Morbi vitae nibh erat, non aliquet diam. Curabitur odio mauris, suscipit non erreting ise ondest 12 teresd en illde</p>
    <div class="more" style="color:var(--orange)">read more &gt;</div>
  </section>
  <section class="abs widget" style="left:637px">
    <div class="widget-bar" style="background:var(--navy)"><svg width="13" height="9" viewBox="0 0 13 9"><rect width="13" height="9" fill="#fff"/><path d="M0 0l6.5 5L13 0" stroke="#10507d" fill="none"/></svg>newsletter</div>
    <div class="date" style="color:var(--navy)">SIGN UP FOR MORE NEWS AND OFFERS</div>
    <div class="field">enter email address...</div>
    <div class="more" style="color:var(--navy);margin-top:10px">send &gt;</div>
  </section>

  <footer class="abs footer"></footer>
  <div class="abs" style="left:160px;top:1022px;width:186px">
    <div class="foot-head">SITEMAP</div>
    <div style="display:flex;gap:40px;margin-top:6px">
      <ul class="foot-links" style="width:66px"><li>Our Service</li><li>Who we are</li><li>Training</li><li>Pay a bill</li><li>Certifications</li><li>Pricing</li></ul>
      <ul class="foot-links"><li>About Us</li><li>Chatterloop</li><li>Blipcast</li><li>News</li><li>Our Story</li><li>Contact</li></ul>
    </div>
  </div>
  <div class="abs" style="left:392px;top:1022px;width:186px"><div class="foot-head">FOLLOW US</div></div>
  <div class="abs fsoc" style="left:409px;top:1050px"></div>
  <div class="abs fsoc" style="left:469px;top:1050px"></div>
  <div class="abs fsoc" style="left:528px;top:1050px"></div>
  <div class="abs fsoc" style="left:409px;top:1086px"></div>
  <div class="abs fsoc" style="left:469px;top:1086px"></div>
  <div class="abs fsoc" style="left:528px;top:1086px"><svg width="12" height="12" viewBox="0 0 14 14" fill="#666"><circle cx="2.5" cy="11.5" r="2"/><path d="M1 6a7 7 0 0 1 7 7h-2a5 5 0 0 0-5-5z"/><path d="M1 1a12 12 0 0 1 12 12h-2A10 10 0 0 0 1 3z"/></svg></div>
  <div class="abs copy" style="left:390px;top:1127px">© Copyright Brightwell 2012 &nbsp;|&nbsp; All rights reserved ®</div>
  <div class="abs" style="left:442px;top:1152px;display:flex;align-items:center;gap:5px">
    <span style="width:14px;height:14px;border-radius:50%;background:#fff"></span>
    <span style="font-family:'PT Sans',sans-serif;font-weight:700;font-size:12px;color:#fff">Brightwell</span>
  </div>

  <div class="abs" style="left:628px;top:1022px;width:182px"><div class="foot-head" style="border:0">CONTACT US</div></div>
  <div class="abs flabel" style="left:630px;top:1047px">Name</div>
  <div class="abs finput" style="left:665px;top:1042px;width:144px;height:19px"></div>
  <div class="abs flabel" style="left:630px;top:1068px">Email</div>
  <div class="abs finput" style="left:665px;top:1064px;width:144px;height:19px"></div>
  <div class="abs flabel" style="left:630px;top:1089px">Message</div>
  <div class="abs finput" style="left:665px;top:1086px;width:144px;height:36px"></div>
  <div class="abs go">GO</div>

</div>
</body>
</html>
```